Lumen Hall of Music Website Design

Lumen Hall of Music would like to have a website designed. They are a new business similar to Quorvale (https://quorvaletunes.example).

We prefer using Adobe Fonts throughout the design. Kepler was used for the logo. Lorem Ipsum is fine to use except for headers.

Please keep track of any images/icons that are used in your design. We plan on purchasing the images used in the winning design.

Target Market(s)

Children age 10 - 18

Number of Pages Required

1 page

Font styles to use
Sans Serif

Colors
0054AA
0677BA
7BADD7
CADEEF
E8F1F8

```html
<!DOCTYPE html>
<html lang="en">
<head>
<meta charset="utf-8">
<title>Lumen Hall of Music</title>
<link href="https://fonts.googleapis.com/css2?family=Rubik:wght@400;500;700;800&display=swap" rel="stylesheet">
<style>
:root{
  --blue:#0054AA;
  --blue-mid:#0677BA;
  --blue-soft:#7BADD7;
  --blue-pale:#CADEEF;
  --blue-wash:#E8F1F8;
  --ink:#1d1d1f;
  --white:#ffffff;
  --line:#dfe3e8;
}
*{margin:0;padding:0;box-sizing:border-box}
html,body{width:785px;height:1200px;overflow:hidden}
body{position:relative;font-family:'Rubik',sans-serif;color:var(--ink);background:var(--white)}
.abs{position:absolute}

/* header */
.site-header{position:absolute;left:0;top:0;width:785px;height:49px;background:var(--blue-wash)}
.brand{position:absolute;left:146px;top:12px;width:60px;text-align:center;color:var(--blue);font-weight:700;font-size:10px;line-height:1.1;letter-spacing:.3px}
.brand small{display:block;font-size:4px;font-weight:700;letter-spacing:.2px}
.brand-dot{width:14px;height:14px;border-radius:50%;background:var(--blue);margin:0 auto 2px}
.nav a{position:absolute;top:21px;font-size:5.2px;font-weight:700;color:var(--ink);text-decoration:none;letter-spacing:.1px}
.nav a.home{color:var(--blue)}
.nav a.about{color:var(--blue-soft)}
.nav .caret{display:inline-block;border-left:2px solid transparent;border-right:2px solid transparent;border-top:2.5px solid var(--ink);margin-left:2px;vertical-align:middle}
.donate{position:absolute;left:506px;top:19px;font-size:5.8px;font-weight:700;color:var(--blue);display:flex;align-items:center;gap:4px}
.btn-register{position:absolute;left:569px;top:13px;width:69px;height:23px;border-radius:12px;background:var(--blue);color:var(--white);font-size:6px;display:flex;align-items:center;justify-content:center}

/* hero */
.hero-copy{position:absolute;left:0;top:49px;width:393px;height:310px;background:var(--blue);color:var(--white)}
.hero-kicker{position:absolute;left:147px;top:63px;font-size:5.6px}
.hero-kicker b{font-weight:700}
.hero-title{position:absolute;left:147px;top:74px;width:230px;font-size:18.2px;font-weight:800;line-height:24.6px}
.hero-text{position:absolute;left:147px;top:153px;width:200px;font-size:4.9px;font-weight:500;line-height:8.2px}
.hero-btn{position:absolute;left:147px;top:190px;width:101px;height:26px;border-radius:13px;background:var(--white);color:var(--ink);font-size:5.8px;display:flex;align-items:center;justify-content:center}
.hero-photo{position:absolute;left:393px;top:49px;width:392px;height:310px;background:linear-gradient(135deg,#e9e6df 0%,#cdbfa9 45%,#6f8fb0 75%,#8a6b4c 100%)}

/* section heads */
.section-title{position:absolute;left:0;width:785px;text-align:center;font-weight:800;font-size:17px}
.section-sub{position:absolute;left:0;width:785px;text-align:center;font-size:4.9px;font-weight:500;line-height:8.2px;text-transform:uppercase}

/* programs */
.program{position:absolute;top:453px;width:90px;height:147px;border:1px solid var(--line);border-radius:3px;background:var(--white);overflow:hidden}
.program-photo{height:82px}
.program h3{font-size:5.7px;font-weight:700;text-align:center;margin-top:5px;white-space:nowrap;overflow:hidden;text-overflow:ellipsis;padding:0 6px}
.program dl{display:grid;grid-template-columns:auto auto;justify-content:space-between;padding:0 7px;font-size:4.8px;row-gap:5px;margin-top:5px}
.program dd{text-align:right}
.program .cta{display:flex;align-items:center;justify-content:center;margin:7px auto 0;width:58px;height:18px;border-radius:9px;background:var(--blue);color:var(--white);font-size:5.8px;font-weight:500}

/* why */
.why{position:absolute;left:0;top:629px;width:785px;height:185px;background:var(--blue-wash)}
.feature{position:absolute;top:696px;width:112px;text-align:center}
.feature-icon{width:30px;height:30px;margin:0 auto;border:1.5px solid var(--blue);border-radius:8px}
.feature h3{font-size:7.2px;font-weight:700;line-height:8px;margin-top:12px;height:16px}
.feature p{font-size:4.9px;font-weight:500;line-height:7px;margin-top:9px}

/* testimonials */
.quote-card{position:absolute;background:var(--white);border:1px solid var(--line);border-radius:3px;overflow:hidden}
.quote-card h4{font-weight:700;text-align:center}
.quote-card p{text-align:center;font-weight:500}
.quote-main{left:236px;top:882px;width:317px;height:92px}
.quote-main h4{font-size:8px;margin-top:15px}
.quote-main p{font-size:4.9px;line-height:8px;margin:9px 40px 0}
.quote-main .author{position:absolute;left:118px;top:62px;display:flex;align-items:center;gap:12px;font-size:5px}
.avatar{border-radius:50%;background:linear-gradient(#7bb3c9,#3f6f7f)}
.quote-side{top:898px;width:147px;height:60px}
.quote-side h4{font-size:5px;margin-top:9px}
.quote-side p{font-size:3px;line-height:5px;margin:6px 10px 0;white-space:nowrap}
.quote-side .author{position:absolute;display:flex;align-items:center;gap:8px;font-size:3px;top:42px}
.arrow{position:absolute;top:918px;width:20px;height:20px;border-radius:50%;background:var(--white);box-shadow:0 1px 3px rgba(0,0,0,.2);display:flex;align-items:center;justify-content:center}

/* footer */
.footer-rule{position:absolute;left:0;width:785px;height:1px;background:var(--line)}
.footer-brand{position:absolute;left:164px;top:1058px;width:60px;text-align:center;color:var(--blue);font-weight:700;font-size:10.5px;line-height:1.1}
.footer-brand small{display:block;font-size:4px}
.footer-brand .brand-dot{width:20px;height:20px;margin-bottom:3px}
.social{position:absolute;top:1130px;width:13px;height:13px;border-radius:50%;background:var(--ink)}
.footer-col{position:absolute;top:1052px}
.footer-col h5{font-size:7px;font-weight:700;letter-spacing:.2px}
.footer-col ul{list-style:none;margin-top:12px}
.footer-col li{font-size:5.8px;font-weight:500;height:18.5px}
.contact p{font-size:5.8px;font-weight:700;height:21px}
.legal{position:absolute;top:1191px;font-size:5.8px;font-weight:500}
</style>
</head>
<body>

<header class="site-header">
  <div class="brand"><div class="brand-dot"></div>LUMEN<small>HALL OF MUSIC</small></div>
  <nav class="nav">
    <a class="home" style="left:223px">HOME</a>
    <a class="about" style="left:251px">ABOUT US</a>
    <a style="left:291px">OUR PROGRAMS<span class="caret"></span></a>
    <a style="left:352px">STUDENT RESOURCES<span class="caret"></span></a>
    <a style="left:430px">SUPPORT QUORVALE<span class="caret"></span></a>
  </nav>
  <div class="donate">DONATE US
    <svg width="10" height="11" viewBox="0 0 10 11"><circle cx="5" cy="4.5" r="4" fill="none" stroke="#0054AA" stroke-width="1"/><text x="5" y="6.5" font-size="5.5" font-weight="700" text-anchor="middle" fill="#0054AA" font-family="Rubik,sans-serif">$</text><path d="M1 10h8" stroke="#0054AA" stroke-width="1"/></svg>
  </div>
  <div class="btn-register">REGISTER</div>
</header>

<section class="hero-copy">
  <div class="hero-kicker"><b>LUMEN</b> HALL OF MUSIC</div>
  <h1 class="hero-title">GET PERFECT MUSIC CLASSES FOR YOUR KIDS</h1>
  <p class="hero-text">Contrary to popular belief, Lorem Ipsum is not simply random text. It has roots in a piece of classical Latin literature from 45 BC, making it over 2000 years old.</p>
  <div class="hero-btn">REGISTER NOW</div>
</section>
<div class="hero-photo" role="img" aria-label="Teacher guiding a young boy playing acoustic guitar on a sofa"></div>

<h2 class="section-title" style="top:385px">Our Programs ?</h2>
<p class="section-sub" style="top:416px">Contrary to popular belief, Lorem Ipsum is not simply random text.<br>It has roots in a piece of classical Latin literature from 45 BC,<br>making it over 2000 years old.</p>

<article class="program" style="left:147px">
  <div class="program-photo" role="img" aria-label="Young child with his mother" style="background:linear-gradient(135deg,#e7d3c3,#c9413a 60%,#d9c2b0)"></div>
  <h3>Early Childhood classes</h3>
  <dl><dt>Age</dt><dd>Newborns – 8 years</dd><dt>Fee Monthly</dt><dd>$175 / Month</dd></dl>
  <div class="cta">Get Class</div>
</article>
<article class="program" style="left:247px">
  <div class="program-photo" role="img" aria-label="Student with headphones at a piano" style="background:linear-gradient(135deg,#8b8a86,#7a2a3a 55%,#5a3d2c)"></div>
  <h3>Private Sessions</h3>
  <dl><dt>Age</dt><dd>4+</dd><dt>Fee Monthly</dt><dd>$175 / Month</dd></dl>
  <div class="cta">Get Class</div>
</article>
<article class="program" style="left:347px">
  <div class="program-photo" role="img" aria-label="Band playing guitars together" style="background:linear-gradient(135deg,#2d4a44,#1c2221 55%,#5b5a55)"></div>
  <h3>Group Classes</h3>
  <dl><dt>Age</dt><dd>6+</dd><dt>Fee Monthly</dt><dd>$175 / Month</dd></dl>
  <div class="cta">Get Class</div>
</article>
<article class="program" style="left:447px">
  <div class="program-photo" role="img" aria-label="Teenagers outdoors at summer camp" style="background:linear-gradient(135deg,#4f7a3a,#8d9aa3 55%,#3d5a2c)"></div>
  <h3>Summer Camps</h3>
  <dl><dt>Age</dt><dd>All ages.</dd><dt>Fee</dt><dd>$175 / Month</dd></dl>
  <div class="cta">Learn More</div>
</article>
<article class="program" style="left:547px">
  <div class="program-photo" role="img" aria-label="Young people dancing and celebrating" style="background:linear-gradient(135deg,#b9bdbc,#6d87a7 55%,#2b2f3a)"></div>
  <h3>Quorvale Music in communities</h3>
  <dl><dt>Age</dt><dd>School age Children</dd><dt>Fee</dt><dd>$175 / Month</dd></dl>
  <div class="cta">Join now</div>
</article>

<section class="why"></section>
<h2 class="section-title" style="top:655px">Why Choose Us ?</h2>
<div class="feature" style="left:149px">
  <div class="feature-icon" role="img" aria-label="Teacher icon"></div>
  <h3>Professional &amp; Trained Teachers</h3>
  <p>Contrary to popular belief, Lorem Ipsum is not simply random text. It has roots in a piece of classical Latin literature from 45 BC, making it over 2000 years old.</p>
</div>
<div class="feature" style="left:274px">
  <div class="feature-icon" role="img" aria-label="Student with guitar icon"></div>
  <h3>Over 5k Students joined us</h3>
  <p>Contrary to popular belief, Lorem Ipsum is not simply random text. It has roots in a piece of classical Latin literature from 45 BC, making it over 2000 years old.</p>
</div>
<div class="feature" style="left:399px">
  <div class="feature-icon" role="img" aria-label="Financial support icon"></div>
  <h3>Financial Support to Students</h3>
  <p>Contrary to popular belief, Lorem Ipsum is not simply random text. It has roots in a piece of classical Latin literature from 45 BC, making it over 2000 years old.</p>
</div>
<div class="feature" style="left:524px">
  <div class="feature-icon" role="img" aria-label="Instruments icon"></div>
  <h3>Very Less Coast for Instrument renting</h3>
  <p>Contrary to popular belief, Lorem Ipsum is not simply random text. It has roots in a piece of classical Latin literature from 45 BC, making it over 2000 years old.</p>
</div>

<h2 class="section-title" style="top:840px">Testimonials !</h2>

<div class="quote-card quote-side" style="left:-1px">
  <h4 style="text-align:left;margin-left:19px">Loved their Classes</h4>
  <p style="text-align:left;margin-left:-30px">popular belief, Lorem Ipsum is not simply random text. It has roots in a piece of<br>classical Latin literature from 45 BC, making it over 2000 years old.</p>
  <div class="author" style="left:18px"><div class="avatar" style="width:13px;height:13px"></div>Marlo Quinn</div>
</div>
<div class="quote-card quote-side" style="left:638px">
  <h4>Loved their Classes</h4>
  <p style="margin-left:28px;text-align:left">Contrary to popular belief, Lorem Ipsum is not simply random text. It has<br>&nbsp;&nbsp;&nbsp;&nbsp;&nbsp;&nbsp;&nbsp;&nbsp;classical Latin literature from 45 BC, making it over 2000 years</p>
  <div class="author" style="left:77px"><div class="avatar" style="width:13px;height:13px"></div>Marlo Quinn</div>
</div>

<div class="arrow" style="left:182px"><svg width="8" height="8" viewBox="0 0 8 8"><path d="M7 4H1M4 1L1 4l3 3" fill="none" stroke="#0054AA" stroke-width="1"/></svg></div>
<div class="arrow" style="left:586px"><svg width="8" height="8" viewBox="0 0 8 8"><path d="M1 4h6M4 1l3 3-3 3" fill="none" stroke="#0054AA" stroke-width="1"/></svg></div>

<div class="quote-card quote-main">
  <h4>Loved their Classes</h4>
  <p>Contrary to popular belief, Lorem Ipsum is not simply random text. It has roots in a piece of classical Latin literature from 45 BC, making it over 2000 years old.</p>
  <div class="author"><div class="avatar" style="width:20px;height:20px"></div>Marlo Quinn</div>
</div>

<div class="footer-rule" style="top:1020px"></div>
<div class="footer-brand"><div class="brand-dot"></div>LUMEN<small>HALL OF MUSIC</small></div>
<div class="social" style="left:147px" role="img" aria-label="Social link"></div>
<div class="social" style="left:167px" role="img" aria-label="Social link"></div>
<div class="social" style="left:188px" role="img" aria-label="Social link"></div>
<div class="social" style="left:208px" role="img" aria-label="Social link"></div>
<div class="social" style="left:228px" role="img" aria-label="Social link"></div>

<div class="footer-col" style="left:297px">
  <h5>NAVIGATIONS</h5>
  <ul><li>Home</li><li>About US</li><li>Our Programs</li><li>Support Quorvale</li><li>Student Resources</li></ul>
</div>
<div class="footer-col" style="left:409px">
  <h5>OUR PROGRAMS</h5>
  <ul><li>Group Classes</li><li>Summer Camps</li><li>Private Sessions</li><li>Early Childhood Classes</li><li>Quorvale Music in communities</li></ul>
</div>
<div class="footer-col contact" style="left:545px">
  <h5>CONTACT US</h5>
  <div style="margin-top:13px"><p>Phone No . +1 555 0142 8890</p><p>Email : hello@lumenhall.example</p></div>
</div>

<div class="footer-rule" style="top:1186px"></div>
<div class="legal" style="left:147px">Lumen Hall of Music</div>
<div class="legal" style="left:529px">Terms &amp; Conditions | Privacy Policy</div>

</body>
</html>
```